Holbrae Structural Approval Standards Private Assessors

Professional Construction Consultancy Company Business Card - must keep logo colours see images below - examples have been added from my last competition - please see them as examples only!

Target Market(s)

Home Builders

Industry/Entity Type

Construction

Contact Information for Business Card

See "must haves"

Font styles to use
Sans Serif

Colors
ffffff
add136
000000

Requirements
Must have
• Daniel Moravi
• Director
• Phone: 0431 587 219
• Address: 7 Tarrunga Rd,
• Hallworth Vale, SA, 5091
• Email: holbraeassessors@mailbox-example.com
• Website: www.holbraeassessors-example.com.au
• Facebook: Holbrae Structural Approval Standards
Nice to have
• Side 1: full logo
• Side 2: company details
Should not have
• hard to read
• must be clear and professional

```html
<!DOCTYPE html>
<html lang="en">
<head>
<meta charset="utf-8">
<title>Holbrae Structural Approval Standards – Business Card</title>
<link rel="stylesheet" href="https://fonts.googleapis.com/css2?family=Lato:wght@400;700&family=Questrial&display=swap">
<style>
  :root {
    --lime: #add136;
    --white: #ffffff;
    --black: #000000;
    --card: #0e1311;
    --card-edge: #050706;
    --backdrop: #2a2a2a;
  }
  * { margin: 0; padding: 0; box-sizing: border-box; }
  html, body { width: 1200px; height: 900px; overflow: hidden; }
  body {
    background: var(--backdrop);
    font-family: "Lato", sans-serif;
    color: var(--white);
    position: relative;
  }
  .card {
    position: absolute;
    left: 325px;
    width: 557px;
    height: 305px;
    background: radial-gradient(ellipse at 50% 35%, #18201c 0%, var(--card) 55%, var(--card-edge) 100%);
    box-shadow: 0 8px 22px rgba(0,0,0,.55);
    display: flex;
    flex-direction: column;
    align-items: center;
  }
  .card--details { top: 129px; padding-top: 82px; }
  .card--brand { top: 477px; justify-content: center; }

  .holder-name {
    font-weight: 700;
    font-size: 27px;
    letter-spacing: 1.5px;
    color: var(--lime);
    text-transform: uppercase;
    line-height: 1;
  }
  .ruled {
    display: flex;
    align-items: center;
    gap: 10px;
    line-height: 1.2;
  }
  .ruled::before, .ruled::after {
    content: "";
    display: block;
    height: 1.5px;
    background: var(--white);
  }
  .holder-role {
    margin-top: 6px;
    font-size: 10px;
    letter-spacing: 6px;
    text-transform: uppercase;
  }
  .holder-role::before, .holder-role::after { width: 26px; }
  .holder-role::after { margin-left: -6px; }

  .company {
    margin-top: 24px;
    font-weight: 700;
    font-size: 14px;
    letter-spacing: 1px;
    color: var(--lime);
  }
  .company::before, .company::after { width: 40px; }
  .address {
    margin-top: 2px;
    font-size: 14px;
    letter-spacing: 2.2px;
    line-height: 1.2;
  }
  .contact-row {
    margin-top: 5px;
    display: flex;
    gap: 14px;
    font-family: "Questrial", sans-serif;
    font-size: 13.5px;
    line-height: 1.2;
  }
  .contact-item { display: flex; align-items: center; gap: 5px; }
  .contact-item svg { width: 11px; height: 11px; fill: var(--lime); }
  .website {
    margin-top: 3px;
    font-family: "Questrial", sans-serif;
    font-size: 13.5px;
  }
  .website::before, .website::after { width: 44px; }
  .website .domain { color: var(--lime); }
  .social {
    margin-top: 27px;
    display: flex;
    align-items: center;
    gap: 10px;
    font-family: "Questrial", sans-serif;
    font-size: 14px;
  }
  .social-mark { width: 15px; height: 15px; background: var(--lime); border-radius: 2px; }

  .brand-name {
    display: flex;
    flex-direction: column;
    align-items: center;
    color: var(--lime);
    font-weight: 700;
    text-transform: uppercase;
    line-height: 1.05;
  }
  .brand-name .brand-main { font-size: 44px; letter-spacing: 2px; }
  .brand-name .brand-line { font-size: 13px; letter-spacing: 2px; margin-top: 4px; }
  .brand-name .brand-sub { margin-top: 6px; font-size: 15px; letter-spacing: 5px; }
</style>
</head>
<body>
  <section class="card card--details">
    <h1 class="holder-name">Daniel Moravi</h1>
    <p class="holder-role ruled">Director</p>
    <p class="company ruled">Holbrae Structural Approval Standards</p>
    <p class="address">7 Tarrunga Rd, Hallworth Vale, SA, 5091</p>
    <div class="contact-row">
      <span class="contact-item">
        <svg viewBox="0 0 24 24" aria-hidden="true"><path d="M6.6 10.8a15.1 15.1 0 0 0 6.6 6.6l2.2-2.2a1 1 0 0 1 1-.25 11.4 11.4 0 0 0 3.6.6 1 1 0 0 1 1 1V20a1 1 0 0 1-1 1A17 17 0 0 1 3 4a1 1 0 0 1 1-1h3.5a1 1 0 0 1 1 1c0 1.25.2 2.45.6 3.6a1 1 0 0 1-.25 1z"/></svg>
        0431 587 219
      </span>
      <span class="contact-item">
        <svg viewBox="0 0 24 24" aria-hidden="true"><path d="M2 6h20v12H2z M2 6l10 7 10-7" fill="none" stroke="#add136" stroke-width="2.5"/></svg>
        holbraeassessors@mailbox-example.com
      </span>
    </div>
    <p class="website ruled"><span>www.<span class="domain">holbraeassessors-example</span>.com.au</span></p>
    <p class="social"><span class="social-mark"></span>Holbrae Structural Approval Standards</p>
  </section>

  <section class="card card--brand">
    <div class="brand-name">
      <span class="brand-main">Holbrae</span>
      <span class="brand-line">Structural Approval Standards</span>
      <span class="brand-sub">Private Assessors</span>
    </div>
  </section>
</body>
</html>
```